Business Card Design

We sell fish products to corporate food companies who then turn these products into final food products for consumers

Industry/Entity Type

Business

Contact Information for Business Card

I need a corporate business card template for a fish products business. We would like it be professional for use in dealing with multi national companies. This company business card template will be used by multiple employees so the following fields must be open to edit (Name, Phone Number and Email address)

```html
<!DOCTYPE html>
<html lang="en">
<head>
<meta charset="utf-8">
<title>Tidewater Seafoods – Business Card</title>
<link rel="stylesheet" href="https://fonts.googleapis.com/css2?family=Open+Sans:wght@400;600;700&display=swap">
<style>
  :root {
    --page-bg: #ecebe8;
    --card-bg: #ffffff;
    --brand-blue: #1f63c6;
    --wordmark-blue: #1d5bb0;
    --ink: #1c1c1c;
    --icon-white: #ffffff;
  }
  html, body {
    margin: 0;
    padding: 0;
    width: 1200px;
    height: 800px;
    overflow: hidden;
    background: var(--page-bg);
  }
  .business-card {
    position: absolute;
    left: 150px;
    top: 143px;
    width: 900px;
    height: 514px;
    background: var(--card-bg);
    box-shadow: 0 6px 22px rgba(0, 0, 0, 0.12);
    font-family: "Open Sans", Arial, sans-serif;
    overflow: hidden;
  }
  .stripe-art {
    position: absolute;
    left: 0;
    top: 0;
    width: 900px;
    height: 514px;
  }
  .stripe { fill: var(--brand-blue); }
  .band-icon { fill: var(--icon-white); }
  .band-icon-line { fill: none; stroke: var(--brand-blue); stroke-width: 1.6; }

  .brand-block {
    position: absolute;
    right: 86px;
    top: 44px;
    width: 460px;
    text-align: center;
    color: var(--wordmark-blue);
    font-weight: 600;
  }
  .brand-dot {
    display: block;
    width: 96px;
    height: 96px;
    margin: 0 auto 14px;
    border-radius: 50%;
    background: var(--wordmark-blue);
  }
  .brand-name {
    margin: 0;
    font-size: 52px;
    line-height: 1;
    letter-spacing: 1px;
  }
  .brand-line {
    margin: 10px 0 0;
    font-size: 30px;
    line-height: 1;
    letter-spacing: 8px;
  }

  .contact-field {
    position: absolute;
    margin: 0;
    color: var(--ink);
    white-space: nowrap;
    line-height: 1.3;
  }
  .contact-name {
    left: 228px;
    top: 290px;
    font-size: 25px;
    font-weight: 700;
  }
  .contact-phone {
    left: 305px;
    top: 390px;
    font-size: 23px;
    font-weight: 400;
  }
  .contact-email {
    left: 280px;
    top: 436px;
    font-size: 23px;
    font-weight: 400;
  }
</style>
</head>
<body>
  <div class="business-card">
    <svg class="stripe-art" viewBox="0 0 900 514" aria-hidden="true">
      <polygon class="stripe" points="60,0 125,0 0,227 0,109"/>
      <polygon class="stripe" points="150,0 215,0 -68,514 -133,514"/>
      <polygon class="stripe" points="180,212 246,212 80,514 14,514"/>
      <polygon class="stripe" points="232,360 298,360 213,514 147,514"/>

      <g class="band-icon" transform="translate(147,297)">
        <circle cx="8" cy="5" r="5"/>
        <path d="M0 19 C0 12 16 12 16 19 Z"/>
      </g>
      <g class="band-icon" transform="translate(233,396)">
        <path d="M3 1 L7 0 L9 5 L6.5 7 C8 10 10 12 13 13.5 L15 11 L20 13 L19 17 C10 18 2 10 3 1 Z"/>
      </g>
      <g transform="translate(209,446)">
        <rect class="band-icon" x="0" y="0" width="18" height="13" rx="1"/>
        <path class="band-icon-line" d="M0.5 0.8 L9 7.5 L17.5 0.8"/>
      </g>
    </svg>

    <div class="brand-block">
      <span class="brand-dot" aria-hidden="true"></span>
      <p class="brand-name">TIDEWATER</p>
      <p class="brand-line">SEAFOODS</p>
    </div>

    <p class="contact-field contact-name">Daniel Reyes</p>
    <p class="contact-field contact-phone">555-012-347</p>
    <p class="contact-field contact-email">dreyes@tidewaterseafoods.com</p>
  </div>
</body>
</html>
```